zipPineLeaf

I have a weebly web site need design and formatted using the color and look and feel similar to another site. Our web site is currently behind password. http://www.zippineleaf.com pwd Lantern7Boat!

I'm looking to layout like https://www.quellbirchhub.com/blog

We want a yellow, light yellow, gray and black as the main colors. Attached image show color of yellow and light yellow. I don't have a specific color for gray and black. If you think there should be addition colors in the color pallet we greatly appreciate your expertise.

We need the logo designed. Right now its just text.

I don't like that our site list the full blog one after another, I like the tiled look, image, tile and small amount of text. Click and go into a blog. Often at the end of a blog you can jump back to main page, and/or see three additional blog tiles. We like how orange carries through on buttons and text, Accent colors are consistent.

I need CSS that can be inserted into each form. If you look at the source of the form, you can see how I tried to format given the form elements. I cannot change the form, but I can easily insert CSS for the form.

I need a template that can be used in Weebly site either you edit on our site or give us a template that can be used.

Industry/Entity Type

Life Coaching

Coding

Coded - Design and coding required

Number of Pages Required

5+ page

Font styles to use
Sans Serif

Requirements
Must have
• What to build a clean color pallet using the Yellow, light yellow I uploaded image. Also a gray and black.

```html
<!DOCTYPE html>
<html lang="en">
<head>
<meta charset="utf-8">
<title>Improvisation — zipPineLeaf</title>
<link href="https://fonts.googleapis.com/css2?family=Oswald:wght@500;600&family=Lato:wght@400;700&family=Roboto:wght@400;500;700&display=swap" rel="stylesheet">
<style>
  :root {
    --yellow: #fdc000;
    --ink: #141414;
    --text: #555555;
    --muted: #8a8a8a;
    --line: #cfcfcf;
    --soft: #f5f5f5;
    --white: #ffffff;
    --share: #4a7ee0;
  }
  * { box-sizing: border-box; margin: 0; padding: 0; }
  html, body { width: 1200px; height: 2795px; overflow: hidden; background: var(--white); }
  body { position: relative; font-family: 'Lato', sans-serif; color: var(--text); }
  .abs { position: absolute; }

  /* header */
  .site-header { position: absolute; left: 0; top: 0; width: 1200px; height: 72px; background: var(--white); }
  .brand { position: absolute; left: 100px; top: 15px; font-family: 'Roboto', sans-serif; font-weight: 700; font-size: 33px; color: #777; letter-spacing: -0.5px; }
  .nav { position: absolute; top: 27px; font-family: 'Roboto', sans-serif; font-weight: 700; font-size: 13.5px; color: var(--ink); }
  .btn-subscribe { position: absolute; left: 940px; top: 15px; width: 159px; height: 40px; background: var(--yellow); color: var(--ink); font-family: 'Roboto', sans-serif; font-weight: 700; font-size: 15px; display: flex; align-items: center; justify-content: center; }

  /* hero */
  .hero { position: absolute; left: 0; top: 72px; width: 1200px; height: 281px;
    background: linear-gradient(100deg, #8c7a9e 0%, #c48b8a 35%, #e9b07a 55%, #8b8fb3 80%, #6f7fa8 100%); }
  .hero h1 { position: absolute; left: 100px; top: 125px; font-family: 'Oswald', sans-serif; font-weight: 600; font-size: 58px; line-height: 68px; color: var(--white); }

  /* article */
  .feature-photo { position: absolute; left: 100px; top: 440px; width: 1000px; height: 490px;
    background: linear-gradient(90deg, #7d8c8e 0%, #5a5048 30%, #8a7565 55%, #6c5a50 75%, #8e9ea3 100%); }
  .category { position: absolute; left: 99px; top: 942px; font-family: 'Roboto', sans-serif; font-weight: 500; font-size: 26px; color: var(--yellow); }
  .share { position: absolute; top: 954px; width: 55px; height: 14px; background: var(--share); border-radius: 2px; }
  .author { position: absolute; left: 948px; top: 944px; font-family: 'Roboto', sans-serif; font-size: 22px; color: var(--muted); display: flex; align-items: center; gap: 8px; }
  .article-body { position: absolute; left: 104px; top: 986px; width: 992px; font-size: 15px; line-height: 25px; }
  .article-body p { margin-bottom: 25px; }

  /* reply */
  .reply { position: absolute; left: 0; top: 1418px; width: 1200px; height: 407px; background: var(--soft); }
  .section-title { position: absolute; width: 1200px; left: 0; text-align: center; font-family: 'Oswald', sans-serif; font-weight: 600; color: var(--ink); }
  .field { position: absolute; background: var(--soft); border: 1px solid var(--line); font-size: 14px; color: #555; padding: 0 11px; display: flex; align-items: center; }
  .notify { position: absolute; left: 0; width: 1200px; top: 1693px; text-align: center; font-size: 10.5px; color: #555; display: flex; justify-content: center; align-items: center; gap: 5px; }
  .notify span.box { width: 11px; height: 11px; border: 1px solid #666; border-radius: 2px; }
  .btn-yellow { position: absolute; background: var(--yellow); color: var(--ink); font-family: 'Roboto', sans-serif; font-weight: 700; display: flex; align-items: center; justify-content: center; }

  /* about */
  .about-text { position: absolute; left: 150px; top: 1963px; width: 900px; text-align: center; font-size: 14.5px; line-height: 24.5px; color: var(--ink); }
  .footer-band { position: absolute; left: 0; top: 2391px; width: 1200px; height: 404px; background: var(--ink); }
  .coach-card { position: absolute; left: 100px; top: 2119px; width: 1000px; height: 362px; background: var(--yellow); }
  .coach-photo { position: absolute; left: 175px; top: 2169px; width: 236px; height: 236px; border-radius: 50%;
    background: radial-gradient(circle at 50% 45%, #b99a86 0%, #7d6e66 45%, #8f9a87 100%); }
  .coach-name { position: absolute; left: 435px; top: 2204px; font-family: 'Roboto', sans-serif; font-weight: 700; font-size: 22px; color: var(--ink); }
  .coach-bio { position: absolute; left: 436px; top: 2237px; width: 600px; font-size: 14.5px; line-height: 25px; color: var(--ink); }
  .btn-outline { position: absolute; left: 436px; top: 2348px; width: 129px; height: 41px; border: 2px solid var(--ink); font-family: 'Roboto', sans-serif; font-weight: 700; font-size: 15px; color: var(--ink); display: flex; align-items: center; justify-content: center; }
  .arrow { position: absolute; top: 2274px; width: 37px; height: 51px; background: var(--ink); display: flex; align-items: center; justify-content: center; }

  /* footer */
  .footer-brand { position: absolute; left: 100px; top: 2547px; font-family: 'Roboto', sans-serif; font-weight: 700; font-size: 37px; color: var(--white); }
  .footer-head { position: absolute; top: 2545px; font-family: 'Roboto', sans-serif; font-weight: 500; font-size: 17.5px; color: var(--white); }
  .footer-links { position: absolute; left: 393px; top: 2580px; list-style: none; font-size: 15.5px; line-height: 31.5px; color: var(--white); }
  .footer-input { position: absolute; left: 622px; top: 2588px; width: 238px; height: 41px; border: 1px solid #888; font-size: 12.5px; color: #ccc; padding-left: 11px; display: flex; align-items: center; }
  .social { position: absolute; top: 2588px; width: 34px; height: 34px; border-radius: 50%; background: var(--white); }
  .footer-rule { position: absolute; left: 100px; top: 2730px; width: 1000px; height: 1px; background: #333; }
  .copyright { position: absolute; left: 0; width: 1200px; top: 2747px; text-align: center; font-size: 15.5px; color: var(--white); }
</style>
</head>
<body>

<header class="site-header">
  <div class="brand">zipPineLeaf</div>
  <span class="nav" style="left:410px">WHO WE ARE</span>
  <span class="nav" style="left:533px">OUR MODEL</span>
  <span class="nav" style="left:649px">WHO USES ZIPPINELEAF</span>
  <span class="nav" style="left:854px">PRICING</span>
  <a class="btn-subscribe">SUBSCRIBE NOW</a>
</header>

<section class="hero" role="img" aria-label="Person in a hoodie raising both arms against a sunset sky">
  <h1>IMPROVISATION</h1>
</section>

<div class="feature-photo" role="img" aria-label="Team of colleagues working together around a table in a bright office"></div>
<div class="category">Finance</div>
<span class="share" style="left:812px"></span>
<span class="share" style="left:877px;width:47px"></span>
<div class="author">
  <svg width="24" height="24" viewBox="0 0 24 24"><circle cx="12" cy="12" r="11" fill="none" stroke="#999" stroke-width="1.5"/><circle cx="12" cy="9.5" r="4" fill="#aaa"/><path d="M4.5 19.5c2-4 13-4 15 0" fill="#aaa"/></svg>
  Coach Rowan
</div>

<article class="article-body">
  <p>Essential to living a joyful life is the ability to adapt to any situation. Life is always going to throw curveballs, and we’re always going to need to find a different way to respond to a new play.</p>
  <p>We need to improvise.</p>
  <p>Improvisation is a fundamental element in cultivating resilience. We may think of improvisation as just making up our moves as we go. But this is an oversimplified definition -- it leaves too much to chance and doesn’t value our existing knowledge and experience. Improvisation is really about calling on our own deep well of experience and working with our environment and the people around us to generate a new response and creative solution to a new situation. Trust that you have the knowledge and experience to try something new, especially if the old way is no longer working for you.</p>
  <p>Find some ways to practice this skill. You may want to start by thinking about a problem you have faced in the past, and use it as an example for yourself to think about all the different solutions to this problem. You can write them down, even the ones you may consider a little crazy. Then you can identify the best solutions and keep them in your back pocket for the next time a similar problem arises.</p>
</article>

<section class="reply"></section>
<h2 class="section-title" style="top:1468px;font-size:43px;line-height:56px">LEAVE A REPLY</h2>
<div class="field" style="left:217px;top:1534px;width:249px;height:44px">Name</div>
<div class="field" style="left:475px;top:1534px;width:250px;height:44px">Email</div>
<div class="field" style="left:735px;top:1534px;width:248px;height:44px">website</div>
<div class="field" style="left:217px;top:1588px;width:766px;height:96px;align-items:flex-start;padding-top:12px;padding-left:9px">Comments</div>
<div class="notify"><span class="box"></span>Notify me of new comments to this post by email</div>
<a class="btn-yellow" style="left:539px;top:1721px;width:122px;height:40px;font-size:15px">SUBMIT</a>

<h2 class="section-title" style="top:1905px;font-size:49px;line-height:62px">WHO WE ARE</h2>
<p class="about-text">We started zipPineLeaf with a passion to help people navigate the multitude of decisions in life and develop a process to create stronger wellbeing.&nbsp; We believe that in order to achieve purpose and fulfillment,&nbsp; you need to focus on your health (physical and mental), career, and finances. Our coaching works with people at any point in life, from Senior in High School to retirement. We help you create a plan and coach you on how execute that plan and reach your goals.</p>

<div class="footer-band"></div>
<div class="coach-card"></div>
<div class="coach-photo" role="img" aria-label="Portrait photo of the coach"></div>
<div class="coach-name">COACH MILO</div>
<p class="coach-bio">I started zipPineLeaf to help others. A coach is not only useful for career professionals and executives -- I want to work with anyone who has the drive to work hard to improve their well being. In my life, I’ve had to overcome a learning disability that I was diagnosed with in second grade, and much later an alcohol and drug addiction.</p>
<a class="btn-outline">READ MORE</a>
<div class="arrow" style="left:82px"><svg width="14" height="26" viewBox="0 0 14 26"><path d="M12 2L2 13l10 11" fill="none" stroke="#fff" stroke-width="1.8"/></svg></div>
<div class="arrow" style="left:1082px"><svg width="14" height="26" viewBox="0 0 14 26"><path d="M2 2l10 11L2 24" fill="none" stroke="#fff" stroke-width="1.8"/></svg></div>

<footer>
  <div class="footer-brand">zipPineLeaf</div>
  <div class="footer-head" style="left:390px">MAIN MENU</div>
  <ul class="footer-links">
    <li>Who We Are</li>
    <li>Our Model</li>
    <li>Who Uses Zippineleaf</li>
    <li>Pricing</li>
  </ul>
  <div class="footer-head" style="left:621px">NEWSLETTER</div>
  <div class="footer-input">Enter Email</div>
  <a class="btn-yellow" style="left:623px;top:2638px;width:115px;height:40px;font-size:16px;font-weight:500">SUBMIT</a>
  <div class="footer-head" style="left:927px">CONTACT US</div>
  <span class="social" style="left:935px"></span>
  <span class="social" style="left:978px"></span>
  <span class="social" style="left:1021px"></span>
  <span class="social" style="left:1063px"></span>
  <div class="footer-rule"></div>
  <div class="copyright">© 2021 zippineleaf. All Rights Reserved.</div>
</footer>

</body>
</html>
```